Create a professional, eye-catching business card design that reflects the values and services of Brookfern Veterinary Hospital. we provide veterinary services and the business card should be a memorable representation of the clinic and align with its branding and mission. our tag line is "Life Long Companions, Lifelong Care"
Use clean, modern typography. Prioritize readability and professionalism. We would like to see designs that use the color blue, as in the logo example. the final design should communicate professionalism and care, with attention to detail.

```html
<!DOCTYPE html>
<html lang="en">
<head>
<meta charset="utf-8">
<title>Brookfern Veterinary Hospital – Business Card</title>
<link href="https://fonts.googleapis.com/css2?family=Montserrat:wght@400;500;700;800&display=swap" rel="stylesheet">
<style>
  :root {
    --navy: #22355a;
    --navy-light: #34497a;
    --card: #ebe6df;
    --card-edge: #f6f3ef;
    --backdrop: #d9d2c8;
    --ink: #1f2b45;
  }
  * { box-sizing: border-box; margin: 0; padding: 0; }
  html, body {
    width: 1200px; height: 1047px; overflow: hidden;
    background: var(--backdrop);
    font-family: "Montserrat", Arial, sans-serif;
  }
  .business-card {
    position: absolute; left: 151px; top: 289px;
    width: 947px; height: 518px;
    background: var(--card);
    border: 2px solid var(--card-edge);
    border-radius: 22px;
    overflow: hidden;
    color: var(--ink);
  }
  .pet-illustration {
    position: absolute; left: 0; bottom: 0;
    width: 420px; height: 400px;
    border-top-right-radius: 60px;
    background: linear-gradient(160deg, var(--navy-light) 0%, var(--navy) 100%);
  }
  .brand {
    position: absolute; left: 688px; top: 30px;
    width: 240px; text-align: center; color: var(--navy);
  }
  .brand-circle {
    width: 110px; height: 110px; margin: 0 auto 14px;
    border: 3px solid var(--navy); border-radius: 50%;
  }
  .brand-name {
    font-weight: 800; font-size: 31px; line-height: 1; letter-spacing: 0.3px;
  }
  .brand-sub {
    font-weight: 800; font-size: 13px; line-height: 1.4; letter-spacing: 0.3px;
  }
  .name-accent {
    position: absolute; right: 0; top: 243px;
    width: 18px; height: 69px; background: var(--navy);
  }
  .person {
    position: absolute; right: 34px; top: 236px; text-align: right;
  }
  .person-name {
    font-weight: 700; font-size: 31px; line-height: 38px; color: var(--navy); letter-spacing: 0.4px;
  }
  .person-role {
    font-weight: 500; font-size: 22px; line-height: 30px; color: var(--ink); margin-top: 6px;
  }
  .tagline {
    position: absolute; right: 34px; top: 333px;
    font-weight: 500; font-size: 22px; line-height: 30px; color: var(--ink);
  }
  .contact-list {
    position: absolute; right: 34px; top: 378px; list-style: none;
  }
  .contact-item {
    display: flex; justify-content: flex-end; align-items: center; gap: 12px;
    font-weight: 500; font-size: 21px; height: 37px; color: var(--ink);
  }
  .contact-icon { width: 19px; height: 19px; fill: var(--navy); }
</style>
</head>
<body>
  <div class="business-card">
    <div class="pet-illustration" role="img" aria-label="Navy silhouette illustration of a cat and a dog sitting on a hill looking up"></div>

    <div class="brand">
      <div class="brand-circle"></div>
      <div class="brand-name">BROOKFERN</div>
      <div class="brand-sub">VETERINARY HOSPITAL</div>
    </div>

    <div class="name-accent"></div>
    <div class="person">
      <div class="person-name">DANIEL MORROW</div>
      <div class="person-role">Managing Director</div>
    </div>

    <div class="tagline">Life Long Companions, Lifelong Care</div>

    <ul class="contact-list">
      <li class="contact-item">123 456 789
        <svg class="contact-icon" viewBox="0 0 24 24"><path d="M3 10c0-3 4-5 9-5s9 2 9 5l-1 2-4-1v-2c-2-.6-6-.6-8 0v2l-4 1zM6 14h12l1 5H5z"/></svg>
      </li>
      <li class="contact-item">info@yourgmail.com
        <svg class="contact-icon" viewBox="0 0 24 24"><path d="M3 9l9-6 9 6v11H3zM5 10l7 5 7-5-7-4z"/></svg>
      </li>
      <li class="contact-item">www.yourwebsite.com
        <svg class="contact-icon" viewBox="0 0 24 24"><path d="M12 2a10 10 0 1 0 0 20 10 10 0 0 0 0-20zm-1 3c-1 2-3 2-3 4s3 1 3 3-2 2-1 5c-3-.5-6-3-6-6s3-5.5 7-6zm3 1c3 1 5 4 5 7-1 0-2-1-3-2s-2 0-2-2 0-2 0-3z"/></svg>
      </li>
    </ul>
  </div>
</body>
</html>
```